Web App Dashboard Design for a Smart Home

We are a company that gives consultancy and installation services for custom smart home designs to household owners in ON, Canada. For our web application, we are in need of a dashboard design which will display multiple rooms that could be present in a home. This should be a flexible design as the number of rooms where smart devices installed will vary from house to house. We would like to see the name of the rooms and several icons that represent different monitored objects in each room like temperature, light on/off, sound/music on/off, humidity, illuminance, noise level, air quality, for bathrooms and kitchens wet/dry conditions, windows/doors open, curtains open/closed etc. The web application will collect the latest status data from all related sensors and it will be publishing the latest status for each room into this dashboard. Backend of the dashboards should contain nice modern looking houses and it would be good if there are multiple versions of the background pictures that rotate.

Target Market(s)

Mid-Market range house holders who want to increase their comfort and safety with smart home implementations

Industry/Entity Type

Small Business

Number of Pages Required

1 page

Colors
0455a3
3277b5
85acd3
86cae7
fbf289
cadf82
acd037
9bcb3c
faa54b

Requirements
Must have
• - A Flexible Dashboard Design which can hold many rooms but still look sharp even with only 1/2 rooms as well.
• - An smart home icon library that will show the monitored value like temperature, lights on/off, door/window open/close etc.

```html
<!DOCTYPE html>
<html lang="en">
<head>
<meta charset="utf-8">
<title>Smart Home Dashboard</title>
<link href="https://fonts.googleapis.com/css2?family=Open+Sans:wght@400;600;700&family=Roboto:wght@500;700&display=swap" rel="stylesheet">
<style>
:root{
  --brand:#0b3f98;
  --page:#eff1f5;
  --white:#ffffff;
  --ink:#2c3440;
  --nav-icon:#0b3f98;
  --orange:#f7963d;
  --steel:#7399c9;
  --sky:#77bde3;
  --green:#8dc12f;
  --navy:#2b62a8;
  --on:#4caf50;
  --off:#e8545a;
  --render-light:#f1f0ec;
  --render-mid:#ddd6ca;
}
*{box-sizing:border-box;margin:0;padding:0}
html,body{width:909px;height:1200px;overflow:hidden}
body{position:relative;background:var(--page);font-family:"Open Sans",Arial,sans-serif;color:var(--white)}
.brand{position:absolute;left:0;top:0;width:174px;height:70px;background:var(--brand);font-family:"Roboto",Arial,sans-serif;font-weight:700;font-size:19px;line-height:70px;padding-left:23px;letter-spacing:.2px}
.topbar{position:absolute;left:174px;top:0;width:735px;height:70px;background:var(--white);border-bottom:1px solid #e3e6eb}
.sidebar{position:absolute;left:0;top:70px;width:174px;height:1130px;background:var(--white);border-right:1px solid #e3e6eb}
.avatar{position:absolute;left:602px;top:12px;width:46px;height:46px;border-radius:50%;background:#d5d7db;overflow:hidden}
.user-name{position:absolute;left:662px;top:28px;font-family:"Roboto",Arial,sans-serif;font-weight:500;font-size:13px;color:var(--ink)}
.logout{position:absolute;left:756px;top:29px;font-family:"Roboto",Arial,sans-serif;font-weight:500;font-size:12px;color:var(--ink);display:flex;align-items:center;gap:4px}
.nav{position:absolute;left:0;top:0;list-style:none}
.nav li{position:absolute;left:22px;width:150px;height:24px;display:flex;align-items:center;font-family:"Roboto",Arial,sans-serif;font-weight:500;font-size:13px;color:var(--ink)}
.nav svg{width:20px;height:20px;margin-right:20px;fill:var(--nav-icon)}
.tile{position:absolute;overflow:hidden}
.tile-label{position:absolute;left:0;width:100%;text-align:center;font-size:13px;font-weight:400;letter-spacing:.2px}
.tile svg{position:absolute}
.orange{background:var(--orange)}.steel{background:var(--steel)}.sky{background:var(--sky)}.green{background:var(--green)}.navy{background:var(--navy)}
.big{position:absolute;font-weight:600}
.value{position:absolute;left:0;width:100%;text-align:center;font-weight:700;font-size:16px}
.toggle{position:absolute;display:flex;height:29px;border:1.5px solid var(--white)}
.toggle span{display:block;width:34px;line-height:26px;text-align:center;font-size:11.5px;font-weight:600}
.toggle .on-active{background:var(--on)}
.toggle .off-active{background:var(--off)}
.toggle .plain{border-left:1px solid var(--white)}
.states{position:absolute;list-style:none}
.states li{display:flex;align-items:center;height:32px;font-weight:700;font-size:15px}
.dot{width:13px;height:13px;border-radius:50%;margin-right:9px;border:2px solid var(--white)}
.dot.filled{background:var(--white)}
.house-view{position:absolute;left:209px;top:709px;width:615px;height:374px;background:var(--white);border:1px solid #e1e4e9}
.house-render{position:absolute;inset:0;background:radial-gradient(ellipse at center,var(--render-mid) 0%,var(--render-light) 75%)}
.copyright{position:absolute;left:209px;top:1136px;width:615px;text-align:center;font-size:10.5px;color:#55595f}
</style>
</head>
<body>
<div class="brand">SMART HOME</div>
<header class="topbar"></header>
<div class="avatar"><svg width="46" height="46" viewBox="0 0 46 46"><circle cx="23" cy="17" r="8" fill="#fff"/><path d="M8 42c2-10 8-14 15-14s13 4 15 14z" fill="#fff"/></svg></div>
<div class="user-name">JANE PARKER</div>
<div class="logout"><svg width="12" height="12" viewBox="0 0 12 12"><path d="M1 1h5v2H3v6h3v2H1z" fill="#7bc043"/><path d="M6 4h3V2l3 4-3 4V8H6z" fill="#7bc043"/></svg>LOG OUT</div>

<aside class="sidebar">
<ul class="nav">
<li style="top:41px"><svg viewBox="0 0 20 20"><path d="M10 2 1 10h3v8h5v-5h2v5h5v-8h3z"/></svg>HOME</li>
<li style="top:92px"><svg viewBox="0 0 20 20"><path d="M10 3a9 9 0 0 0-9 9c0 2 .6 3.6 1.6 5h14.8c1-1.4 1.6-3 1.6-5a9 9 0 0 0-9-9zm0 11a2 2 0 0 1-1-3.7L12 6l-1 5.6A2 2 0 0 1 10 14z"/></svg>DASHBOARD</li>
<li style="top:142px"><svg viewBox="0 0 20 20"><path d="M10 1 1 5v2h18V5zM3 8h2v8H3zm4 0h2v8H7zm4 0h2v8h-2zm4 0h2v8h-2zM1 17h18v2H1z"/></svg>COMPANY</li>
<li style="top:193px"><svg viewBox="0 0 20 20"><path d="M1 3h18v11H1zm2 2v7h14V5zM8 15h4v2h3v1H5v-1h3z"/></svg>MONITORING</li>
<li style="top:244px"><svg viewBox="0 0 20 20"><path d="M10 2a8 8 0 0 0-8 8v6h4v-6H4a6 6 0 0 1 12 0h-2v6h4v-6a8 8 0 0 0-8-8z"/></svg>SUPPORT</li>
</ul>
</aside>

<main>
<section class="tile orange" style="left:209px;top:112px;width:229px;height:168px">
  <div class="tile-label" style="top:20px">TEMPERATURE</div>
  <svg style="left:23px;top:52px" width="46" height="70" viewBox="0 0 46 70"><path d="M12 6a7 7 0 0 1 14 0v38a13 13 0 1 1-14 0z" fill="none" stroke="#fff" stroke-width="3.5"/><circle cx="19" cy="55" r="7" fill="#fff"/><rect x="17" y="22" width="4" height="30" fill="#fff"/><path d="M32 10h10M32 18h10M32 26h10M32 34h6" stroke="#fff" stroke-width="3"/></svg>
  <div style="position:absolute;left:91px;top:62px;width:1px;height:52px;background:rgba(255,255,255,.45)"></div>
  <div class="big" style="left:108px;top:66px;font-size:34px;line-height:40px">19.9<sup style="font-size:16px;vertical-align:16px">0</sup> c</div>
  <div class="value" style="top:131px;font-size:15.5px">MODE : HEAT</div>
</section>

<section class="tile steel" style="left:450px;top:112px;width:180px;height:78px">
  <div class="tile-label" style="top:8px">LIGHT</div>
  <svg style="left:27px;top:32px" width="28" height="40" viewBox="0 0 28 40"><path d="M14 3a11 11 0 0 0-7 19c2 2 3 4 3 6h8c0-2 1-4 3-6a11 11 0 0 0-7-19z" fill="none" stroke="#fff" stroke-width="2.5"/><rect x="9" y="30" width="10" height="4" fill="#fff"/><rect x="10" y="35" width="8" height="3" rx="1.5" fill="#fff"/></svg>
  <div class="toggle" style="left:78px;top:37px"><span class="on-active">ON</span><span class="plain">OFF</span></div>
</section>

<section class="tile sky" style="left:643px;top:112px;width:180px;height:78px">
  <div class="tile-label" style="top:8px">HUMIDITY</div>
  <svg style="left:25px;top:29px" width="26" height="36" viewBox="0 0 26 36"><path d="M13 1C9 10 2 17 2 24a11 11 0 0 0 22 0c0-7-7-14-11-23z" fill="#fff"/><path d="M7 23a6 6 0 0 0 5 7" stroke="#77bde3" stroke-width="2" fill="none"/></svg>
  <div class="big" style="left:78px;top:27px;font-size:32px;line-height:40px">20%</div>
</section>

<section class="tile sky" style="left:450px;top:202px;width:180px;height:78px">
  <div class="tile-label" style="top:8px">MUSIC</div>
  <svg style="left:24px;top:32px" width="36" height="40" viewBox="0 0 36 40"><path d="M12 8 33 2v26" stroke="#fff" stroke-width="4" fill="none"/><path d="M12 8v24" stroke="#fff" stroke-width="4"/><ellipse cx="7" cy="32" rx="7" ry="5.5" fill="#fff"/><ellipse cx="28" cy="28" rx="7" ry="5.5" fill="#fff"/></svg>
  <div class="toggle" style="left:81px;top:37px"><span>ON</span><span class="off-active">OFF</span></div>
</section>

<section class="tile steel" style="left:643px;top:202px;width:180px;height:78px">
  <div class="tile-label" style="top:8px">ILLUMINANCE</div>
  <svg style="left:18px;top:29px" width="40" height="40" viewBox="0 0 40 40"><circle cx="20" cy="20" r="10" fill="none" stroke="#fff" stroke-width="3"/><g stroke="#fff" stroke-width="4" stroke-linecap="round"><path d="M20 2v4M20 34v4M2 20h4M34 20h4M7 7l3 3M30 30l3 3M7 33l3-3M30 10l3-3"/></g></svg>
  <div class="big" style="left:67px;top:38px;font-size:16px;font-weight:400">200 to 300 lx</div>
</section>

<section class="tile steel" style="left:209px;top:293px;width:197px;height:173px">
  <div class="tile-label" style="top:21px">NOISE LEVEL</div>
  <svg style="left:60px;top:54px" width="78" height="62" viewBox="0 0 78 62"><g fill="#fff"><rect x="0" y="14" width="16" height="4"/><rect x="0" y="24" width="16" height="4"/><rect x="0" y="34" width="16" height="4"/><rect x="0" y="44" width="16" height="4"/><rect x="0" y="54" width="16" height="4"/><rect x="20" y="34" width="16" height="4"/><rect x="20" y="44" width="16" height="4"/><rect x="20" y="54" width="16" height="4"/><rect x="41" y="0" width="16" height="4"/><rect x="41" y="10" width="16" height="4"/><rect x="41" y="20" width="16" height="4"/><rect x="41" y="30" width="16" height="4"/><rect x="41" y="40" width="16" height="4"/><rect x="41" y="50" width="16" height="4"/><rect x="62" y="20" width="16" height="4"/><rect x="62" y="30" width="16" height="4"/><rect x="62" y="40" width="16" height="4"/><rect x="62" y="50" width="16" height="4"/></g></svg>
  <div class="value" style="top:134px">86.3 DBA</div>
</section>

<section class="tile green" style="left:418px;top:293px;width:197px;height:173px">
  <div class="tile-label" style="top:21px">AIR QUALITY</div>
  <svg style="left:50px;top:52px" width="96" height="66" viewBox="0 0 96 66"><g fill="none" stroke="#fff" stroke-width="3" stroke-linecap="round"><path d="M8 6c14-6 24 10 40 4s22-8 38-4"/><path d="M80 0l6 6-7 5"/><path d="M88 30c-14-6-24 10-40 4s-22-8-38-4"/><path d="M16 24l-6 6 7 5"/><path d="M8 56c14-6 24 10 40 4s22-8 38-4"/><path d="M80 50l6 6-7 5"/></g></svg>
  <div class="value" style="top:134px">89 IAQ</div>
</section>

<section class="tile sky" style="left:626px;top:293px;width:197px;height:173px">
  <div class="tile-label" style="top:21px">BATHROOMS</div>
  <svg style="left:20px;top:57px" width="78" height="66" viewBox="0 0 78 66"><path d="M58 30V8a6 6 0 0 1 12 0v22" fill="none" stroke="#fff" stroke-width="4"/><path d="M58 8h-6" stroke="#fff" stroke-width="3"/><path d="M62 16c-2 3-3 5-1 6s3-3 1-6z" fill="#fff"/><path d="M0 30h78c0 14-8 24-22 24H22C8 54 0 44 0 30z" fill="#fff"/><path d="M12 52l-3 10h6l3-8zM66 52l3 10h-6l-3-8z" fill="#fff"/></svg>
  <ul class="states" style="left:126px;top:59px"><li><span class="dot filled"></span>WET</li><li><span class="dot"></span>DRY</li></ul>
</section>

<section class="tile steel" style="left:209px;top:478px;width:197px;height:173px">
  <div class="tile-label" style="top:21px">KITCHENS</div>
  <svg style="left:24px;top:62px" width="74" height="60" viewBox="0 0 74 60"><g fill="none" stroke="#fff" stroke-width="3"><rect x="2" y="2" width="26" height="56"/><rect x="36" y="2" width="36" height="18"/><path d="M46 11h16"/><rect x="28" y="34" width="44" height="24"/><path d="M50 34v24M34 44h10M56 42h10"/><path d="M22 22v12"/></g><g fill="#fff"><circle cx="58" cy="50" r="1.5"/><circle cx="64" cy="50" r="1.5"/></g></svg>
  <ul class="states" style="left:121px;top:60px"><li><span class="dot filled"></span>WET</li><li><span class="dot"></span>DRY</li></ul>
</section>

<section class="tile sky" style="left:418px;top:478px;width:197px;height:173px">
  <div class="tile-label" style="top:21px">WINDOWS/DOORS</div>
  <svg style="left:17px;top:61px" width="75" height="75" viewBox="0 0 75 75"><g fill="none" stroke="#fff" stroke-width="4"><rect x="2" y="2" width="71" height="71" rx="5"/><path d="M14 65V38a23 23 0 0 1 46 0v27z"/><path d="M37 15v50M14 38h46M37 38l-16-16M37 38l16-16"/></g><circle cx="33" cy="54" r="2" fill="#fff"/><circle cx="41" cy="54" r="2" fill="#fff"/></svg>
  <ul class="states" style="left:107px;top:60px"><li><span class="dot"></span>OPEN</li><li><span class="dot filled"></span>CLOSED</li></ul>
</section>

<section class="tile navy" style="left:626px;top:478px;width:197px;height:173px">
  <div class="tile-label" style="top:21px">CURTAINS</div>
  <svg style="left:26px;top:60px" width="68" height="65" viewBox="0 0 68 65"><g fill="#fff"><rect x="0" y="8" width="68" height="3"/><rect x="3" y="2" width="3" height="14"/><rect x="11" y="2" width="3" height="14"/><rect x="19" y="2" width="3" height="14"/><rect x="27" y="2" width="3" height="14"/><rect x="38" y="2" width="3" height="14"/><rect x="46" y="2" width="3" height="14"/><rect x="54" y="2" width="3" height="14"/><rect x="62" y="2" width="3" height="14"/><rect x="1" y="19" width="28" height="36"/><rect x="39" y="19" width="28" height="36"/><rect x="1" y="59" width="28" height="5"/><rect x="39" y="59" width="28" height="5"/></g></svg>
  <ul class="states" style="left:107px;top:60px"><li><span class="dot filled"></span>OPEN</li><li><span class="dot filled"></span>CLOSED</li></ul>
</section>

<section class="house-view">
  <div class="house-render" role="img" aria-label="3D cutaway render of a furnished modern apartment"></div>
</section>
</main>

<footer class="copyright">Copyright © 2019, Smart Home. All rights reserved.</footer>
</body>
</html>
```